Disability Service Provider needs a flyer

Project Description:
We are seeking a creative and engaging flyer design to promote a twelve week independent living skills program, focusing on key areas such as money management, basic cooking, food safety, and personal well-being and interpersonal skills. The flyer will be used to encourage individuals to enhance their abilities to live independently and confidently.

Target Audience:
Our target audience includes young adults with a disability and individuals transitioning into independent living situations. We aim to reach those who may be new to managing their own finances, cooking for themselves, and maintaining a healthy lifestyle.

Key Messages:

Independent Living Skills: Emphasize the importance of acquiring essential skills for independent living.
Money Management: Highlight budgeting tips, saving strategies, and financial planning.
Basic Cooking: Showcase simple recipes, cooking techniques, and meal preparation tips.
Food Safety: Provide information on safe food handling practices, storage guidelines, and hygiene.
Personal Well-being: Promote self-care practices, stress management techniques, and mental health awareness.

Target Market(s)

Young adults looking to live independently on their own or with friends

Industry/Entity Type

community services sector

Colors
0054AA
0677BA
7BADD7
CADEEF
E8F1F8

Requirements
Must have
• refer to brief

```html
<!DOCTYPE html>
<html lang="en">
<head>
<meta charset="utf-8">
<title>Brightpath Care – Independent Living Skills Program Flyer</title>
<link rel="stylesheet" href="https://fonts.googleapis.com/css2?family=Noto+Serif:wght@400;700&display=swap">
<style>
  :root {
    --navy: #0054AA;
    --ocean: #0677BA;
    --sky: #7BADD7;
    --mist: #CADEEF;
    --ice: #E8F1F8;
    --stage: #0A72B5;
    --white: #ffffff;
  }
  * { box-sizing: border-box; margin: 0; padding: 0; }
  html, body { width: 1200px; height: 800px; overflow: hidden; }
  body {
    background: var(--stage);
    font-family: "Noto Serif", Georgia, serif;
    position: relative;
  }
  .flyer {
    position: absolute;
    left: 330px; top: 18px;
    width: 540px; height: 764px;
    overflow: hidden;
    background: var(--mist);
    box-shadow: 0 10px 24px rgba(0, 30, 70, .35);
  }
  .flyer-shapes { position: absolute; inset: 0; width: 540px; height: 764px; }
  .hero-photo { position: absolute; left: 0; top: 20px; width: 540px; height: 230px; }
  .brand {
    position: absolute; right: 28px; top: 24px;
    display: flex; align-items: center; gap: 8px;
    color: var(--white); font-weight: 700; font-size: 20px;
  }
  .brand-dot { width: 14px; height: 14px; border-radius: 50%; background: var(--sky); }
  .hero-title {
    position: absolute; left: 0; right: 0; top: 114px;
    text-align: center; color: var(--white);
    font-weight: 700; font-size: 24px; line-height: 30px; letter-spacing: .5px;
  }
  .hero-subtitle {
    position: absolute; left: 0; right: 0; top: 198px;
    text-align: center; color: var(--white);
    font-weight: 700; font-size: 17px; line-height: 21px;
  }
  .section-heading {
    position: absolute; color: var(--navy);
    font-weight: 700; font-size: 18px; line-height: 22px; letter-spacing: .6px;
  }
  .about-heading { left: 28px; top: 346px; }
  .services-heading { left: 252px; top: 346px; }
  .about-lead {
    position: absolute; left: 28px; top: 380px; width: 190px;
    color: var(--navy); font-weight: 700; font-size: 14.5px; line-height: 15.5px; letter-spacing: .3px;
  }
  .about-body {
    position: absolute; left: 28px; top: 452px; width: 190px;
    color: var(--ocean); font-size: 10.6px; line-height: 14.6px; letter-spacing: .4px;
  }
  .about-tagline {
    position: absolute; left: 28px; top: 574px; width: 205px;
    color: var(--navy); font-weight: 700; font-size: 14.5px; line-height: 19px; letter-spacing: .3px;
  }
  .service {
    position: absolute; left: 252px; width: 272px;
    display: flex; gap: 12px;
  }
  .service-marker { flex: none; width: 34px; height: 36px; margin-top: -4px; }
  .service-text { color: var(--ocean); font-size: 10.6px; line-height: 14.6px; letter-spacing: .4px; }
  .service-text strong { color: var(--navy); font-size: 13.5px; font-weight: 700; letter-spacing: .3px; }
  .contact {
    position: absolute; left: 28px; top: 664px; color: var(--white);
  }
  .contact-heading { font-weight: 700; font-size: 14px; margin-bottom: 7px; letter-spacing: .3px; }
  .contact-row {
    display: flex; align-items: flex-start; gap: 7px;
    font-weight: 700; font-size: 10.4px; line-height: 11.5px; margin-bottom: 7px; letter-spacing: .3px;
  }
  .contact-row.phone { font-size: 13px; line-height: 14px; }
  .contact-icon { width: 14px; height: 14px; flex: none; }
  .hours {
    position: absolute; right: 20px; top: 738px;
    width: 182px;
    color: var(--navy); font-weight: 700; font-size: 8.6px; line-height: 10px; letter-spacing: .3px;
  }
</style>
</head>
<body>
<main class="flyer">
  <svg class="flyer-shapes" viewBox="0 0 540 764" aria-hidden="true">
    <defs>
      <linearGradient id="heroTone" x1="0" y1="0" x2="1" y2="1">
        <stop offset="0" stop-color="#4C6F93"/>
        <stop offset=".5" stop-color="#6F8FB3"/>
        <stop offset="1" stop-color="#5C84B4"/>
      </linearGradient>
    </defs>
    <rect width="540" height="340" fill="var(--navy)"/>
    <path d="M0 20 H270 C290 20 300 70 330 70 H540 V340 H0 Z" fill="url(#heroTone)"/>
    <path d="M0 230 C120 330 320 345 540 275 V310 C360 340 160 345 0 330 Z" fill="var(--sky)"/>
    <path d="M0 200 C110 300 320 310 540 245 V278 C320 340 120 325 0 232 Z" fill="var(--navy)"/>
    <path d="M250 322 C370 318 470 296 540 280 V296 C470 310 380 326 250 330 Z" fill="var(--ocean)"/>
    <path d="M0 326 C160 344 360 334 540 300 V764 H0 Z" fill="var(--mist)"/>
    <path d="M0 638 H185 L200 648 H0 Z" fill="var(--sky)"/>
    <path d="M210 648 L300 718 H540 V764 H300 Z" fill="var(--sky)"/>
    <path d="M0 648 H212 L323 764 H0 Z" fill="var(--navy)"/>
  </svg>

  <div class="hero-photo" role="img" aria-label="Photo of a young woman working on a laptop at a table beside house plants"></div>

  <div class="brand"><span class="brand-dot"></span>Brightpath Care</div>

  <h1 class="hero-title">LIVE INDEPENDENTLY<br>AND CONFIDENTLY</h1>
  <p class="hero-subtitle">Twelve Week Independent<br>Living Skills Program</p>

  <h2 class="section-heading about-heading">ABOUT US</h2>
  <p class="about-lead">We Help enhance the lives of those with disabilities, aging adults and their families.</p>
  <p class="about-body">At Brightpath Care we pride ourselves in helping you implement your NDIS plan: by providing tailored services, experienced support workers and connecting you to suitable Allied health professionals.</p>
  <p class="about-tagline">Your Trusted Partner in Disability &amp; Independent Living Support Services.</p>

  <h2 class="section-heading services-heading">OUR SUPPORT SERVICES</h2>

  <div class="service" style="top:386px">
    <svg class="service-marker" viewBox="0 0 34 36"><path d="M0 0 H20 L34 18 L20 36 H0 L10 18 Z" fill="var(--navy)"/><circle cx="9" cy="18" r="7.5" fill="var(--sky)" stroke="var(--navy)"/><text x="9" y="21" font-size="7" font-weight="700" text-anchor="middle" fill="var(--navy)" font-family="Noto Serif, serif">01</text></svg>
    <p class="service-text"><strong>Independent Living Skills:</strong><br>Emphasize the importance of acquiring essential skills for independent living.</p>
  </div>
  <div class="service" style="top:459px">
    <svg class="service-marker" viewBox="0 0 34 36"><path d="M0 0 H20 L34 18 L20 36 H0 L10 18 Z" fill="var(--navy)"/><circle cx="9" cy="18" r="7.5" fill="var(--sky)" stroke="var(--navy)"/><text x="9" y="21" font-size="7" font-weight="700" text-anchor="middle" fill="var(--navy)" font-family="Noto Serif, serif">02</text></svg>
    <p class="service-text"><strong>Money Management:</strong> Highlight budgeting tips, saving strategies, and financial planning.</p>
  </div>
  <div class="service" style="top:517px">
    <svg class="service-marker" viewBox="0 0 34 36"><path d="M0 0 H20 L34 18 L20 36 H0 L10 18 Z" fill="var(--navy)"/><circle cx="9" cy="18" r="7.5" fill="var(--sky)" stroke="var(--navy)"/><text x="9" y="21" font-size="7" font-weight="700" text-anchor="middle" fill="var(--navy)" font-family="Noto Serif, serif">03</text></svg>
    <p class="service-text"><strong>Basic Cooking:</strong> Showcase simple recipes, cooking techniques, and meal preparation tips.</p>
  </div>
  <div class="service" style="top:575px">
    <svg class="service-marker" viewBox="0 0 34 36"><path d="M0 0 H20 L34 18 L20 36 H0 L10 18 Z" fill="var(--navy)"/><circle cx="9" cy="18" r="7.5" fill="var(--sky)" stroke="var(--navy)"/><text x="9" y="21" font-size="7" font-weight="700" text-anchor="middle" fill="var(--navy)" font-family="Noto Serif, serif">04</text></svg>
    <p class="service-text"><strong>Food Safety:</strong> Provide information on safe food handling practices, storage guidelines, and hygiene.</p>
  </div>
  <div class="service" style="top:633px">
    <svg class="service-marker" viewBox="0 0 34 36"><path d="M0 0 H20 L34 18 L20 36 H0 L10 18 Z" fill="var(--navy)"/><circle cx="9" cy="18" r="7.5" fill="var(--sky)" stroke="var(--navy)"/><text x="9" y="21" font-size="7" font-weight="700" text-anchor="middle" fill="var(--navy)" font-family="Noto Serif, serif">05</text></svg>
    <p class="service-text"><strong>Personal Well-being:</strong> Promote self-care practices, stress management techniques, and mental health awareness.</p>
  </div>

  <section class="contact">
    <h3 class="contact-heading">Get In Touch</h3>
    <div class="contact-row">
      <svg class="contact-icon" viewBox="0 0 14 14"><circle cx="7" cy="7" r="7" fill="var(--white)"/><path d="M7 2.5a3 3 0 0 0-3 3c0 2.2 3 5.8 3 5.8s3-3.6 3-5.8a3 3 0 0 0-3-3z" fill="var(--navy)"/><circle cx="7" cy="5.5" r="1.1" fill="var(--white)"/></svg>
      <span>7/45 Harbour Lane,<br>Riverside QLD 4000</span>
    </div>
    <div class="contact-row">
      <svg class="contact-icon" viewBox="0 0 14 14"><circle cx="7" cy="7" r="7" fill="var(--white)"/><rect x="3.5" y="4.5" width="7" height="5" rx=".6" fill="var(--navy)"/><path d="M3.8 4.8 L7 7.3 L10.2 4.8" stroke="var(--white)" stroke-width=".8" fill="none"/></svg>
      <span>hello@brightpathcare.com.au</span>
    </div>
    <div class="contact-row phone">
      <svg class="contact-icon" viewBox="0 0 14 14"><circle cx="7" cy="7" r="7" fill="var(--white)"/><path d="M4.6 3.4c.4-.3.8-.2 1 .2l.7 1.3c.2.3.1.6-.2.8l-.5.4c.4 1 1.2 1.8 2.2 2.3l.4-.5c.2-.3.6-.4.9-.2l1.3.7c.4.2.5.7.2 1l-.6.7c-.4.4-1 .5-1.6.3C6.4 9.7 4.3 7.6 3.6 5.6c-.2-.6 0-1.2.4-1.6z" fill="var(--navy)"/></svg>
      <span>1300 555 019</span>
    </div>
  </section>

  <p class="hours">Our support centre is open Monday to Friday 9 am to 5 pm (local time)</p>
</main>
</body>
</html>
```